Packaging for Portable Bidet Product

Product:
Our product, Swishka, is a portable hand bidet. What is a portable hand bidet as some may ask? It is small water bottle with a nozzle head that is used to wash “bottoms” after going “poo-poo” (pardon our crudeness). Bidets are popular in European, Asian and African markets and are used alongside toilet paper to give a truly fresh and clean experience. Besides cleanliness, bidets are eco-friendly (they reduce toilet paper usage by x%) and are perfect for travel.
Current Competition + Role of Packaging:
We are launching our portable bidet product in the US market, primarily to be sold via Marketvale. There are currently some existing players in the market, but we’ve done our research and created a product that is superior in functionality and style. That being said, our competitors still have a first-mover advantage and have amassed a high volume of Marketvale ratings, hence we have a bit of a challenge which we feel that can be easily tackled with premium branding and marketing.
That being said, we are looking for a packaging design that:
i. Distinguishing our product on Marketvale (meaning, the packaging looks good in photos)
ii. Highlight that ours is a premium product
Our design values:
‘Hygiene meets modern design’. Some adjectives that describe our brand -
• Clean
• Fresh
• Simple
• Quirky
• Premium
• Discreet
• Subtle
Attachments:
• Our packaging dimensions (see attached)
• Our brand color (Pantone 331C)
• Our logo file (see attached file)
• Product photos (see attached file)
• Illustration of our product instructions (see attached file)
• Packaging designs that inspire us (see attached file)
• Packaging designs of our competition for reference (see attached file)
• Content/text for the packaging box (see below)
What should be on the box:
• Logo and Brand Name
• Product Photo (can be an outline/illustration as well)
• Product instructions illustration (see attached file)
• Text to be included in packaging
o Product description – “A Modern Portable Bidet”
o Bottle size – 400ml
o Key features
Anti-leak
Discreet design
Travel friendly size
Angled spray
Eco-friendly
Easy squeeze bottle
Includes travel bag
Target Market(s)
The product is aimed at both men and women (of all ages) in the US and Canada markets. In terms of audience targets, we will be appealing to outdoor enthusiasts, immigrants abroad, new parents (product to be used to clean their babies), patients (people with limited mobility) and eco-conscious consumers.
Industry/Entity Type
Health And Wellness

```html
<!DOCTYPE html>
<html lang="en">
<head>
<meta charset="utf-8">
<title>Swishka – Portable Bidet Carton Dieline</title>
<link rel="stylesheet" href="https://fonts.googleapis.com/css2?family=Montserrat:wght@700;800&display=swap">
<style>
  :root {
    --cyan: #41c4e7;
    --green: #13684a;
    --mint: #a9dcd6;
    --ink: #111111;
    --white: #ffffff;
    --paper: #ffffff;
    --step-fill: rgba(255, 255, 255, 0.22);
  }
  html, body {
    margin: 0;
    padding: 0;
    width: 898px;
    height: 1200px;
    overflow: hidden;
    background: var(--paper);
  }
  .dieline {
    display: block;
    width: 898px;
    height: 1200px;
    font-family: "Montserrat", sans-serif;
  }
  .board { fill: var(--cyan); }
  .brand-dot { fill: var(--green); }
  .brand-name {
    fill: var(--green);
    font-weight: 800;
    text-anchor: middle;
    letter-spacing: -1.5px;
  }
  .brand-name--faint { fill: var(--mint); }
  .brand-dot--faint { fill: var(--mint); }
  .label {
    fill: var(--green);
    font-weight: 800;
    text-anchor: middle;
    letter-spacing: 1px;
  }
  .feature {
    fill: var(--green);
    font-weight: 800;
    text-anchor: middle;
    font-size: 13.5px;
    letter-spacing: 1px;
  }
  .volume {
    fill: var(--ink);
    font-weight: 800;
    font-size: 19px;
    text-anchor: end;
  }
  .step-art { fill: var(--step-fill); stroke: var(--white); stroke-width: 1.6; }
  .step-badge { fill: var(--cyan); stroke: var(--white); stroke-width: 1.4; }
  .step-number { fill: var(--white); font-weight: 700; font-size: 12px; text-anchor: middle; }
</style>
</head>
<body>
<svg class="dieline" viewBox="0 0 1650 2205" xmlns="http://www.w3.org/2000/svg">
  <defs>
    <linearGradient id="water" x1="0" y1="0" x2="1" y2="0">
      <stop offset="0" stop-color="#dcf1fb"/>
      <stop offset="0.07" stop-color="#6fb6e6"/>
      <stop offset="0.16" stop-color="#2f6fc9"/>
      <stop offset="0.26" stop-color="#7fc8ef"/>
      <stop offset="0.36" stop-color="#3a8ad4"/>
      <stop offset="0.46" stop-color="#8fd2f3"/>
      <stop offset="0.7" stop-color="#b9e5f8"/>
      <stop offset="1" stop-color="#d6f0fb"/>
    </linearGradient>
  </defs>

  <!-- Glue flap -->
  <polygon class="board" points="123,805 232,765 232,1545 123,1497"/>

  <!-- Top tuck flap -->
  <path class="board" d="M232,765 V425 Q232,410 247,410 H529 Q544,410 544,425 V765 Z"/>
  <g class="tuck-mark" transform="rotate(180 388 600)">
    <text class="brand-name brand-name--faint" x="388" y="695" font-size="52">swishka</text>
    <circle class="brand-dot brand-dot--faint" cx="388" cy="570" r="62"/>
  </g>

  <!-- Panel 1: front -->
  <rect class="board" x="232" y="765" width="312" height="780"/>
  <g role="img" aria-label="Product photo: flowing water, ice cubes and two portable bidet bottles">
    <rect x="232" y="765" width="312" height="780" fill="url(#water)"/>
  </g>
  <circle class="brand-dot" cx="392" cy="872" r="58"/>
  <text class="brand-name" x="388" y="1015" font-size="44">swishka</text>
  <text class="label" x="388" y="1054" font-size="15">A MODERN PORTABLE BIDET</text>
  <text class="volume" x="530" y="1530">400ml</text>
  <path class="board" d="M232,1545 H544 V1765 H456 L449,1755 V1682 H326 V1755 L316,1765 H232 Z"/>

  <!-- Panel 2: side with instructions -->
  <polygon class="board" points="556,614 756,614 816,680 816,765 544,765 556,740"/>
  <rect class="board" x="544" y="765" width="272" height="780"/>
  <circle class="brand-dot" cx="680" cy="872" r="58"/>
  <text class="brand-name" x="680" y="1015" font-size="44">swishka</text>
  <text class="label" x="678" y="1054" font-size="15">PRODUCT DESCRIPTION</text>
  <g class="steps">
    <g role="img" aria-label="Step 1 illustration: fill the bottle with water">
      <circle class="step-art" cx="672" cy="1104" r="40"/>
      <circle class="step-badge" cx="691" cy="1140" r="10"/>
      <text class="step-number" x="691" y="1144">1</text>
    </g>
    <g role="img" aria-label="Step 2 illustration: attach the nozzle">
      <circle class="step-art" cx="672" cy="1200" r="40"/>
      <circle class="step-badge" cx="691" cy="1236" r="10"/>
      <text class="step-number" x="691" y="1240">2</text>
    </g>
    <g role="img" aria-label="Step 3 illustration: angle the spray">
      <circle class="step-art" cx="672" cy="1297" r="40"/>
      <circle class="step-badge" cx="691" cy="1333" r="10"/>
      <text class="step-number" x="691" y="1337">3</text>
    </g>
    <g role="img" aria-label="Step 4 illustration: squeeze the bottle">
      <circle class="step-art" cx="672" cy="1393" r="40"/>
      <circle class="step-badge" cx="691" cy="1429" r="10"/>
      <text class="step-number" x="691" y="1433">4</text>
    </g>
    <g role="img" aria-label="Step 5 illustration: store in the travel bag">
      <circle class="step-art" cx="672" cy="1489" r="40"/>
      <circle class="step-badge" cx="691" cy="1525" r="10"/>
      <text class="step-number" x="691" y="1529">5</text>
    </g>
  </g>
  <polygon class="board" points="544,1545 816,1545 816,1765 700,1765 689,1752 689,1680"/>

  <!-- Panel 3: back -->
  <rect class="board" x="816" y="763" width="309" height="790"/>
  <g role="img" aria-label="Product photo: flowing water, ice cubes and two portable bidet bottles">
    <rect x="816" y="763" width="309" height="790" fill="url(#water)"/>
  </g>
  <circle class="brand-dot" cx="973" cy="872" r="58"/>
  <text class="brand-name" x="972" y="1015" font-size="44">swishka</text>
  <text class="volume" x="1110" y="1536">400ml</text>
  <polygon class="board" points="816,1553 1125,1553 1030,1688 1030,1765 1020,1773 918,1773 908,1760 908,1688"/>

  <!-- Panel 4: features -->
  <polygon class="board" points="1180,614 1388,614 1388,738 1400,765 1128,765 1128,698"/>
  <rect class="board" x="1125" y="765" width="275" height="788"/>
  <circle class="brand-dot" cx="1262" cy="856" r="44"/>
  <text class="brand-name" x="1262" y="948" font-size="30">swishka</text>
  <text class="label" x="1262" y="1004" font-size="16">KEY FEATURES</text>
  <g class="features">
    <text class="feature" x="1268" y="1050">ANTI-LEAK</text>
    <text class="feature" x="1268" y="1126">DISCREET DESIGN</text>
    <text class="feature" x="1268" y="1201">TRAVEL FRIENDLY SIZE</text>
    <text class="feature" x="1268" y="1277">ANGLED SPRAY</text>
    <text class="feature" x="1268" y="1352">ECO-FRIENDLY</text>
    <text class="feature" x="1268" y="1428">EASY SQUEEZE BOTTLE</text>
    <text class="feature" x="1268" y="1503">INCLUDES TRAVEL BAG</text>
  </g>
  <polygon class="board" points="1127,1553 1400,1553 1255,1690 1255,1765 1245,1775 1127,1775"/>
</svg>
</body>
</html>
```